Website for Nonprofit for kids whose parents have been wounded

We need a web design for a nonprofit that serves children who have been severely burned as well as those whose parents have been wounded during military service. We will be based out of hospitals and will need a format that will encourage trust, safety, and respect. We are stick with a lot of red white and blue. We will also be looking to have a space for donations.

Target Market(s)

Kids and parents of military veterans

Industry/Entity Type

Non Profit

Number of Pages Required

5+ page

Font styles to use
Serif
Decorative

Colors
ec1f27
ffffff
0255a3

Requirements
Must have
• Be both appealing to children and adults. Create a reputable face for our organization. We need an area for donations.
Nice to have
• Something unique

```html
<!DOCTYPE html>
<html lang="en">
<head>
<meta charset="utf-8">
<title>Kinhaven – Caring for Military Families</title>
<link rel="stylesheet" href="https://fonts.googleapis.com/css2?family=PT+Serif:wght@400;700&family=Open+Sans:wght@400;600;700&display=swap">
<style>
  :root {
    --red: #ec1f27;
    --blue: #0255a3;
    --white: #ffffff;
    --ink: #3a3a3a;
    --muted: #6d6d6d;
    --rule: #d9d9d9;
    --footer: #2b2b2b;
    --footer-deep: #222222;
    --footer-text: #c9c9c9;
  }
  * { box-sizing: border-box; margin: 0; padding: 0; }
  html, body { width: 798px; height: 1200px; overflow: hidden; }
  body {
    position: relative;
    background: var(--white);
    font-family: "Open Sans", Arial, sans-serif;
    font-size: 10.5px;
    line-height: 1.45;
    color: var(--muted);
  }
  a { color: inherit; text-decoration: none; }
  ul { list-style: none; }

  /* Header */
  .site-header { position: absolute; left: 0; top: 0; width: 798px; height: 90px; }
  .brand { position: absolute; left: 20px; top: 24px; }
  .brand-name { font-family: "Open Sans", Arial, sans-serif; font-weight: 600; font-size: 22px; color: var(--ink); letter-spacing: 0; }
  .search-box {
    position: absolute; left: 519px; top: 14px; width: 266px; height: 52px;
    background: var(--blue); border-radius: 6px; padding: 16px 14px;
    display: flex; align-items: center;
  }
  .search-input { flex: 1; height: 20px; background: var(--white); border: 0; font-size: 9px; color: #888; padding: 0 6px; line-height: 20px; }
  .search-button { width: 22px; height: 20px; background: var(--red); display: flex; align-items: center; justify-content: center; }

  .main-nav {
    position: absolute; left: 13px; top: 92px; width: 772px; height: 30px;
    background: var(--red); display: flex; align-items: center; padding-left: 10px;
  }
  .main-nav a {
    color: var(--white); font-size: 12px; font-weight: 600; padding: 0 21px;
    border-right: 1px solid rgba(255,255,255,.45); line-height: 14px;
  }
  .main-nav a:last-child { border-right: 0; }

  /* Hero */
  .hero { position: absolute; left: 13px; top: 128px; width: 772px; height: 212px; }
  .hero-photo { width: 100%; height: 100%; background: linear-gradient(100deg, #c9c2b8 0%, #e6e0d6 35%, #d8cfc4 60%, #b9b2ac 100%); }
  .hero-dots { position: absolute; left: 0; right: 0; bottom: 10px; display: flex; justify-content: center; gap: 6px; }
  .hero-dots span { width: 7px; height: 7px; border-radius: 50%; background: rgba(255,255,255,.7); }
  .hero-dots span.active { background: var(--red); }

  /* Section headings */
  .section-title {
    font-family: "PT Serif", Georgia, serif; font-size: 14px; font-weight: 400;
    color: var(--ink); text-transform: uppercase; letter-spacing: .5px;
    padding-bottom: 6px; border-bottom: 1px solid var(--rule); margin-bottom: 10px;
  }
  .column { position: absolute; top: 362px; width: 246px; }
  .col-vision { left: 13px; }
  .col-services { left: 274px; }
  .col-donate { left: 539px; }

  .vision-item { display: flex; gap: 8px; margin-bottom: 16px; }
  .vision-thumb { flex: 0 0 74px; height: 58px; background: linear-gradient(135deg, #b58a62, #d8c3a4); }
  .vision-thumb.ward { background: linear-gradient(135deg, #8fa7c2, #d7dde4); }
  .vision-title { font-weight: 700; font-size: 10.5px; color: var(--ink); }
  .vision-text { font-size: 9.5px; }
  .read-more { display: block; text-align: right; color: var(--blue); font-size: 10px; font-weight: 600; margin-top: 3px; }

  .services-list { margin: 8px 0 8px 4px; }
  .services-list li { display: flex; align-items: center; gap: 7px; color: var(--red); font-family: "PT Serif", Georgia, serif; font-size: 11px; line-height: 15px; }

  .donate-photo { width: 246px; height: 110px; background: linear-gradient(135deg, #a98566, #d9c8b4 55%, #c2a98f); margin-bottom: 8px; }

  .section-rule { position: absolute; left: 13px; top: 650px; width: 772px; border-top: 1px solid var(--rule); }

  /* About */
  .about { position: absolute; left: 13px; top: 676px; width: 507px; }
  .about-intro { color: #8a8a8a; font-size: 9.5px; margin-bottom: 14px; }
  .about-body { display: flex; gap: 14px; }
  .about-photo { flex: 0 0 140px; height: 118px; background: linear-gradient(160deg, #c4b08f, #9c7c5c 60%, #7b8c9b); margin-left: 8px; }
  .about-text { font-size: 10px; padding-top: 4px; }
  .about .read-more { margin-top: 4px; }

  .events { position: absolute; left: 539px; top: 676px; width: 246px; }
  .event { display: flex; gap: 10px; margin-bottom: 24px; align-items: flex-start; }
  .event-thumb { flex: 0 0 46px; height: 46px; background: linear-gradient(135deg, #c69a5a, #e7c98f); }
  .event-thumb.art { background: linear-gradient(135deg, #7d9bc4, #d5b36c); }
  .event-thumb.run { background: linear-gradient(135deg, #b56f4b, #e3c596); }
  .event-text { color: var(--blue); font-size: 10.5px; font-weight: 600; line-height: 1.35; }

  /* Footer */
  .site-footer { position: absolute; left: 13px; top: 931px; width: 772px; height: 254px; background: var(--footer); color: var(--footer-text); }
  .footer-col { position: absolute; top: 22px; }
  .footer-col h3 { font-family: "PT Serif", Georgia, serif; font-weight: 400; font-size: 12.5px; color: var(--white); margin-bottom: 10px; }
  .footer-col li { font-size: 9.5px; line-height: 14px; }
  .fc-links { left: 19px; } .fc-services { left: 160px; } .fc-address { left: 307px; }
  .fc-contact { left: 471px; width: 282px; }
  .form-row { display: flex; gap: 12px; }
  .field { flex: 1; }
  .field label { display: block; font-size: 9.5px; margin-bottom: 3px; }
  .field .box { height: 20px; background: #3a3a3a; border: 1px solid #4a4a4a; }
  .field .box.tall { height: 60px; }
  .form-actions { display: flex; gap: 8px; margin-top: 10px; }
  .btn { width: 52px; height: 20px; background: #454545; border: 1px solid #5a5a5a; color: var(--white); font-size: 9.5px; text-align: center; line-height: 18px; }
  .footer-bottom { position: absolute; left: 0; bottom: 0; width: 100%; height: 34px; border-top: 1px solid #3c3c3c; background: var(--footer-deep); padding: 10px 19px; font-size: 9.5px; }
</style>
</head>
<body>

<header class="site-header">
  <a class="brand" href="#"><span class="brand-name">Kinhaven</span></a>
  <form class="search-box">
    <div class="search-input">Search the website...</div>
    <div class="search-button">
      <svg width="10" height="10" viewBox="0 0 10 10"><path d="M3 1 L7 5 L3 9" stroke="#fff" stroke-width="1.6" fill="none"/></svg>
    </div>
  </form>
</header>

<nav class="main-nav">
  <a href="#">Home</a><a href="#">About</a><a href="#">Services</a><a href="#">Photo Gallery</a><a href="#">Donate Us</a><a href="#">Contact Us</a>
</nav>

<section class="hero">
  <div class="hero-photo" role="img" aria-label="Children drawing together at a table in a bright playroom"></div>
  <div class="hero-dots"><span class="active"></span><span></span><span></span><span></span></div>
</section>

<section class="column col-vision">
  <h2 class="section-title">Our Vision - Mission</h2>
  <article class="vision-item">
    <div class="vision-thumb" role="img" aria-label="Volunteer reading with a child"></div>
    <div>
      <h3 class="vision-title">Caring for little heroes</h3>
      <p class="vision-text">We stand beside children and families through every step of recovery.</p>
      <a class="read-more" href="#">Continue Reading »</a>
    </div>
  </article>
  <article class="vision-item">
    <div class="vision-thumb ward" role="img" aria-label="Hospital family room"></div>
    <div>
      <h3 class="vision-title">Safe spaces in hospitals</h3>
      <p class="vision-text">Quiet rooms, kind hands and play help every child feel at home.</p>
      <a class="read-more" href="#">Continue Reading »</a>
    </div>
  </article>
</section>

<section class="column col-services">
  <h2 class="section-title">Our Services</h2>
  <p>We bring comfort, play and care to kids in hospital wards across the country.</p>
  <ul class="services-list">
    <li><svg width="7" height="8" viewBox="0 0 7 8"><path d="M0 0 L7 4 L0 8Z" fill="#0255a3"/></svg>Bedside play visits</li>
    <li><svg width="7" height="8" viewBox="0 0 7 8"><path d="M0 0 L7 4 L0 8Z" fill="#0255a3"/></svg>Family support circles</li>
    <li><svg width="7" height="8" viewBox="0 0 7 8"><path d="M0 0 L7 4 L0 8Z" fill="#0255a3"/></svg>Burn recovery camps</li>
    <li><svg width="7" height="8" viewBox="0 0 7 8"><path d="M0 0 L7 4 L0 8Z" fill="#0255a3"/></svg>Homework help</li>
    <li><svg width="7" height="8" viewBox="0 0 7 8"><path d="M0 0 L7 4 L0 8Z" fill="#0255a3"/></svg>Holiday gift drives</li>
    <li><svg width="7" height="8" viewBox="0 0 7 8"><path d="M0 0 L7 4 L0 8Z" fill="#0255a3"/></svg>Parent respite care</li>
    <li><svg width="7" height="8" viewBox="0 0 7 8"><path d="M0 0 L7 4 L0 8Z" fill="#0255a3"/></svg>Travel and meal aid</li>
  </ul>
  <p>Each program is free for military families and their children.</p>
</section>

<section class="column col-donate">
  <h2 class="section-title">Donate Us</h2>
  <div class="donate-photo" role="img" aria-label="Row of neatly made children's beds in a shelter room"></div>
  <p>Your gift brings toys, meals and warm beds to children in need. Every dollar helps a family stay close.</p>
</section>

<div class="section-rule"></div>

<section class="about">
  <h2 class="section-title">About Us</h2>
  <p class="about-intro">We are a family of volunteers, nurses and veterans who believe every child deserves comfort, courage and care while a parent heals.</p>
  <div class="about-body">
    <div class="about-photo" role="img" aria-label="Historic hospital building on a town street"></div>
    <p class="about-text">Founded inside a military hospital, we began with one playroom and a box of crayons. Today our teams visit wards each week, host family nights and give parents a moment to rest. We keep every visit safe, gentle and full of respect.</p>
  </div>
  <a class="read-more" href="#">Continue Reading »</a>
</section>

<section class="events">
  <h2 class="section-title">Upcoming Events</h2>
  <article class="event">
    <div class="event-thumb" role="img" aria-label="Families at an outdoor picnic"></div>
    <p class="event-text">Family picnic day at the park this spring</p>
  </article>
  <article class="event">
    <div class="event-thumb art" role="img" aria-label="Children's paintings on a table"></div>
    <p class="event-text">Art night for kids in the hospital ward</p>
  </article>
  <article class="event">
    <div class="event-thumb run" role="img" aria-label="Runners at a charity race"></div>
    <p class="event-text">Annual benefit run for military families</p>
  </article>
</section>

<footer class="site-footer">
  <div class="footer-col fc-links">
    <h3>Quick Links</h3>
    <ul><li>Home</li><li>About Us</li><li>Our Mission</li><li>Programs</li><li>Photo Gallery</li><li>Events</li><li>Donate Now</li><li>Contact Us</li></ul>
  </div>
  <div class="footer-col fc-services">
    <h3>Services</h3>
    <ul><li>Play Visits</li><li>Family Support</li><li>Burn Recovery</li><li>Homework Help</li><li>Gift Drives</li><li>Respite Care</li><li>Travel Aid</li><li>Volunteer</li></ul>
  </div>
  <div class="footer-col fc-address">
    <h3>Address</h3>
    <ul><li>Kinhaven Project Inc</li><li>120 Liberty Way</li><li>Suite 4</li><li>Fairview, VA 22030</li><li>Phone: (555) 014-2280</li><li>hello@kinhaven.org</li></ul>
  </div>
  <div class="footer-col fc-contact">
    <h3>Why Not Contact Us Today !</h3>
    <div class="form-row">
      <div class="field"><label>Name</label><div class="box"></div></div>
      <div class="field"><label>Email</label><div class="box"></div></div>
    </div>
    <div class="field" style="margin-top:8px"><label>Message</label><div class="box tall"></div></div>
    <div class="form-actions"><div class="btn">Send</div><div class="btn">Reset</div></div>
  </div>
  <div class="footer-bottom">Copyright © 2013 Kinhaven Project INC - All Rights Reserved</div>
</footer>

</body>
</html>
```